Flyer Template Design

I have attached 4 files. I would like a design template that could be used across these documents so that they have a common look and feel. The content of the documents is tested and should not be changed significantly. The images can be changed. I have also attache our logo for color compatibility.
Updates

Need extra days to review

Target Market(s)

Wealthy Christian donors

Font styles to use
Serif
Sans Serif

```html
<!DOCTYPE html>
<html lang="en">
<head>
<meta charset="utf-8">
<title>The Harvest Fund – Finishing the Great Commission</title>
<link rel="stylesheet" href="https://fonts.googleapis.com/css2?family=Source+Sans+3:ital,wght@0,400;0,600;0,700;1,600;1,700&display=swap">
<style>
  :root {
    --white: #ffffff;
    --sky: #1b9ad6;
    --ocean: #12609f;
    --navy: #0a2f63;
    --leaf: #9cc23a;
    --leaf-text: #a6cf3c;
    --ink: #1f2a3a;
    --grey: #5b6068;
    --brand-navy: #15305a;
  }
  * { box-sizing: border-box; margin: 0; padding: 0; }
  html, body {
    width: 969px; height: 1200px; overflow: hidden;
    background: var(--white);
  }
  .flyer {
    position: relative; width: 969px; height: 1200px; overflow: hidden;
    font-family: "Source Sans 3", "Helvetica Neue", Arial, sans-serif;
    color: var(--white);
  }
  .backdrop { position: absolute; inset: 0; }

  .brand {
    position: absolute; left: 48px; top: 82px;
    display: flex; align-items: center; gap: 14px;
  }
  .brand-dot { width: 26px; height: 26px; border-radius: 50%; background: var(--sky); }
  .brand-name {
    font-weight: 600; font-size: 32px; line-height: 1;
    color: var(--brand-navy); white-space: nowrap;
  }

  .headline {
    position: absolute; left: 43px; top: 268px;
    font-weight: 700; font-size: 48px; line-height: 54px;
    letter-spacing: 0.3px; text-transform: uppercase;
  }

  .column { position: absolute; }
  .column-left { left: 43px; top: 396px; width: 424px; }
  .column-right { left: 506px; top: 400px; width: 415px; }

  .intro {
    font-weight: 700; font-size: 17px; line-height: 22.6px;
    text-align: justify; hyphens: auto;
  }
  .section-title {
    font-weight: 700; font-style: italic; font-size: 18px;
    color: var(--leaf-text); text-transform: uppercase;
    letter-spacing: 0.3px; margin: 24px 0 6px 14px;
  }
  .column-right .section-title:first-child { margin-top: 0; }
  .body-copy { font-size: 14.2px; line-height: 18.7px; }
  .body-copy + .body-copy { margin-top: 18px; }
  .callout {
    font-weight: 700; font-style: italic; font-size: 14.6px;
    color: var(--leaf-text); margin-top: 20px;
  }

  .action {
    position: absolute; left: 0; top: 904px; width: 969px;
    padding: 0 40px 0 43px; text-align: center;
  }
  .action-title {
    font-weight: 700; font-size: 21px; letter-spacing: 0.4px;
    text-transform: uppercase; margin-bottom: 16px;
  }
  .action-copy {
    font-size: 15.4px; line-height: 25px; text-align: left;
  }

  .closing { position: absolute; left: 0; top: 1076px; width: 969px; text-align: center; }
  .closing-line { font-style: italic; font-weight: 600; font-size: 23px; color: var(--ink); }
  .contact { margin-top: 12px; font-size: 15px; line-height: 25px; color: var(--grey); }
  .contact strong { font-weight: 700; }
</style>
</head>
<body>
<main class="flyer">
  <svg class="backdrop" width="969" height="1200" viewBox="0 0 969 1200" aria-hidden="true">
    <defs>
      <linearGradient id="blueField" x1="0" y1="0" x2="0" y2="1">
        <stop offset="0" stop-color="#1b9ad6"/>
        <stop offset="0.45" stop-color="#12609f"/>
        <stop offset="1" stop-color="#0a2f63"/>
      </linearGradient>
      <linearGradient id="portraitTones" x1="0" y1="0" x2="1" y2="1">
        <stop offset="0" stop-color="#8a4a33"/>
        <stop offset="0.35" stop-color="#b5352c"/>
        <stop offset="0.65" stop-color="#c98a4a"/>
        <stop offset="1" stop-color="#5a3a2a"/>
      </linearGradient>
    </defs>
    <polygon points="0,164 969,365 969,900 0,900" fill="url(#blueField)"/>
    <polygon points="0,854 969,882 969,1025 0,1060" fill="var(--leaf)"/>
  </svg>

  <svg class="portraits" role="img" aria-label="Collage of portraits of people from many nations in traditional dress"
       width="969" height="370" viewBox="0 0 969 370" style="position:absolute;left:0;top:0">
    <polygon points="420,0 969,0 969,365 343,233" fill="url(#portraitTones)"/>
  </svg>

  <div class="brand">
    <span class="brand-dot"></span>
    <span class="brand-name">The Harvest Fund</span>
  </div>

  <h1 class="headline">Finishing the<br>Great Commission</h1>

  <section class="column column-left">
    <p class="intro">Before Jesus ascended into heaven, He commanded his apostles, “Go and make disciples of all nations.” For more than 2000 years the church has been working to fulfill this “Great Commission,” and much has been accomplished. But now, for the first time in history, our generation has the real opportunity to finish the Great Commission in our lifetimes.</p>
    <h2 class="section-title">It’s about nations</h2>
    <p class="body-copy">In the Bible, the word “nations” refers to people groups: groups of people who share a common ethnicity, culture, and language. So when Jesus said, “Go and make disciples if all nations,” He was telling us to take the gospel to every people group on earth.</p>
    <p class="body-copy">Amazingly, there are about 12,000 of these people groups scattered throughout the world. And the Great Commission commands us to make disciples in every one of them.</p>
  </section>

  <section class="column column-right">
    <h2 class="section-title">Where do we stand?</h2>
    <p class="body-copy">Today, there are still about 500 people groups who have never heard the gospel. Most of these groups are small and located in remote, difficult places. These remaining “unengaged” people groups have no known believers. But now that we know who and where these groups are, by God’s grace it is possible that we can engage every one of them with the gospel within the next 3 years.</p>
    <p class="callout">In other words, we can finish the Great Commission!</p>
    <h2 class="section-title">Hastening his coming</h2>
    <p class="body-copy">The Bible says that believers “ought to live holy and godly lives, looking for and hastening the coming of the day of God.” It also says that day will not come until the gospel has been preached to “all nations.” So how can hasten the day of his coming? By finishing the work he gave us to do: making disciples in all nations.</p>
  </section>

  <section class="action">
    <h2 class="action-title">You can make that happen</h2>
    <p class="action-copy">Partner with the Harvest Fund and finance the missionaries who are taking the gospel for the first time to those last remaining people groups. Your investment will “hasten the coming of the day of God” by accelerating the effort to make “disciples in every nation.” In 2018, our partners helped take the gospel to 231 people groups in 35 countries.</p>
  </section>

  <footer class="closing">
    <p class="closing-line">Join us as we invest to make disciples in “all nations” by 2022.</p>
    <p class="contact">To learn more, email Daniel Crane at <strong>dcrane@harvestfund.org</strong><br>www.harvestfund.org</p>
  </footer>
</main>
</body>
</html>
```